Design Packaging for Monte Alba Coffee

Please look at website at www.montealbacoffeecompany.example
Need packaging for new coffee company. The size is: 6 x 9 x 3"

```html
<!DOCTYPE html>
<html lang="en">
<head>
<meta charset="utf-8">
<title>Monte Alba Coffee – Costa Rica Coffee Bag</title>
<link rel="stylesheet" href="https://fonts.googleapis.com/css2?family=Oswald:wght@400;500;600&family=Jost:wght@500;600&display=swap">
<style>
  :root {
    --backdrop: #d9eff4;
    --cream: #ecdc9c;
    --cream-light: #f3e6ae;
    --label-cream: #dccd8c;
    --red-bright: #d42a22;
    --red-deep: #a0102e;
    --crimson: #7c0624;
    --black: #0d0b0b;
    --ink: #111111;
    --brand-brown: #8a5a22;
    --side-red: #c0201c;
    --side-text: #b49a5a;
  }
  * { margin: 0; padding: 0; box-sizing: border-box; }
  html, body {
    width: 1200px;
    height: 900px;
    overflow: hidden;
    background: var(--backdrop);
  }
  .dieline {
    position: absolute;
    left: 240px;
    top: 90px;
    width: 720px;
    height: 720px;
    display: flex;
  }

  /* Front panel */
  .front-panel {
    position: relative;
    width: 480px;
    height: 720px;
    overflow: hidden;
    background: linear-gradient(180deg,
      var(--red-bright) 12%,
      var(--red-deep) 40%,
      var(--red-bright) 68%,
      var(--crimson) 88%,
      var(--black) 100%);
  }
  .brand-band {
    position: absolute;
    left: 0; top: 0;
    width: 100%;
    height: 82px;
    background: var(--cream);
    display: flex;
    align-items: center;
    justify-content: center;
    gap: 10px;
  }
  .brand-dot {
    width: 16px;
    height: 16px;
    border-radius: 50%;
    background: var(--brand-brown);
  }
  .brand-name {
    font-family: "Oswald", sans-serif;
    font-weight: 600;
    font-size: 24px;
    letter-spacing: 0.5px;
    color: var(--brand-brown);
    text-transform: uppercase;
  }
  .product-title {
    position: absolute;
    left: 0; top: 100px;
    width: 100%;
    text-align: center;
    font-family: "Oswald", sans-serif;
    font-weight: 500;
    color: var(--cream-light);
    text-transform: uppercase;
    line-height: 0.95;
  }
  .product-title .origin { display: block; font-size: 72px; letter-spacing: -1px; }
  .product-title .kind { display: block; font-size: 116px; letter-spacing: -2px; }

  .leaf-spray {
    position: absolute;
    left: 330px; top: 330px;
    width: 150px;
    height: 190px;
    border-radius: 40% 10% 40% 20%;
    background: linear-gradient(160deg, #f0a020 0%, #e07a12 60%, rgba(224,122,18,0) 100%);
    z-index: 1;
  }
  .toucan-art {
    position: absolute;
    left: 0; top: 470px;
    width: 150px;
    height: 250px;
    border-radius: 0 70% 0 0;
    background: linear-gradient(150deg,
      #f2b51a 0%, #e45a1c 25%, #1a1414 50%, #0f0c0c 100%);
    z-index: 1;
  }
  .info-label {
    position: absolute;
    left: 110px; top: 335px;
    width: 255px;
    height: 290px;
    background: var(--label-cream);
    font-family: "Jost", sans-serif;
    font-weight: 600;
    color: var(--ink);
    text-align: center;
    text-transform: uppercase;
    z-index: 2;
  }
  .info-label .claim {
    position: absolute;
    top: 50px; left: 0; width: 100%;
    font-size: 22px;
    letter-spacing: 7px;
    line-height: 1.25;
  }
  .info-label .blend {
    position: absolute;
    top: 210px; left: 0; width: 100%;
    font-size: 21px;
    letter-spacing: 5px;
    line-height: 1.3;
  }
  .weight-tab {
    position: absolute;
    left: 110px; bottom: 0;
    width: 255px;
    height: 58px;
    background: var(--label-cream);
    display: flex;
    align-items: center;
    justify-content: center;
    font-family: "Jost", sans-serif;
    font-weight: 600;
    font-size: 22px;
    letter-spacing: 4px;
    color: var(--ink);
    z-index: 2;
  }

  /* Side gusset */
  .side-panel {
    position: relative;
    width: 240px;
    height: 720px;
    background: var(--black);
    padding: 300px 34px 0;
  }
  .side-brand {
    display: flex;
    align-items: center;
    gap: 6px;
    font-family: "Oswald", sans-serif;
    font-weight: 600;
    font-size: 14px;
    text-transform: uppercase;
    color: var(--brand-brown);
  }
  .side-brand .brand-dot { width: 9px; height: 9px; }
  .side-title {
    margin-top: 14px;
    font-family: "Oswald", sans-serif;
    font-weight: 500;
    font-size: 20px;
    text-transform: uppercase;
    color: var(--side-red);
  }
  .side-copy {
    margin-top: 10px;
    font-family: "Oswald", sans-serif;
    font-weight: 400;
    font-size: 12px;
    line-height: 1.9;
    text-transform: uppercase;
    letter-spacing: 0.4px;
    color: var(--side-text);
    text-align: justify;
  }
</style>
</head>
<body>
  <main class="dieline">
    <section class="front-panel">
      <header class="brand-band">
        <span class="brand-dot"></span>
        <span class="brand-name">Monte Alba Coffee</span>
      </header>

      <h1 class="product-title">
        <span class="origin">Costa Rica</span>
        <span class="kind">Coffee</span>
      </h1>

      <div class="leaf-spray" role="img" aria-label="Illustration of orange tropical leaves with red coffee cherries"></div>

      <div class="toucan-art" role="img" aria-label="Illustration of a toucan with a yellow and orange beak among orange leaves"></div>

      <div class="info-label">
        <p class="claim">Premium<br>Product</p>
        <p class="blend">100%<br>Arabica</p>
      </div>

      <div class="weight-tab">700gr</div>
    </section>

    <aside class="side-panel">
      <div class="side-brand">
        <span class="brand-dot"></span>
        <span>Monte Alba Coffee</span>
      </div>
      <h2 class="side-title">Costa Rica Coffee</h2>
      <p class="side-copy">Grown on volcanic slopes in the central highlands, these beans are picked by hand at full ripeness, washed in mountain spring water and dried slowly under the sun. Roasted in small batches to bring out notes of honey, citrus and dark chocolate with a bright, clean finish. Store sealed in a cool dry place and brew fresh.</p>
    </aside>
  </main>
</body>
</html>
```